Vexmora Stationary
Project: Vexmora Stationary
Vexmora Stationary - Information Technology
Creative Brief
Modern
Mathieu Ferrand
Associate
Av. Pierre Dumel 42 CH-1209 Geneva
mferrand@vexmora.com
www.vexmora.com

```html
<!DOCTYPE html>
<html lang="en">
<head>
<meta charset="utf-8">
<title>Vexmora Stationery</title>
<link rel="stylesheet" href="https://fonts.googleapis.com/css2?family=Montserrat:wght@400;500;700&display=swap">
<style>
  :root {
    --backdrop: #ececec;
    --card-white: #ffffff;
    --card-dark: #3a3a3a;
    --brand-blue: #2f8fd8;
    --ink: #2b2b2b;
    --ink-soft: #6a6a6a;
    --on-dark: #ffffff;
  }
  * { box-sizing: border-box; margin: 0; padding: 0; }
  html, body {
    width: 1200px; height: 906px; overflow: hidden;
    background: var(--backdrop);
    font-family: "Montserrat", sans-serif;
  }
  .stationery {
    position: relative; width: 1200px; height: 906px;
    display: flex; align-items: center; justify-content: center; gap: 60px;
  }
  .card {
    position: relative; width: 520px; height: 297px;
    box-shadow: 0 10px 30px rgba(0,0,0,0.12);
  }
  .card--front { background: var(--card-white); }
  .card--back {
    background: var(--card-dark);
    display: flex; align-items: center; justify-content: center;
  }
  .brand {
    position: absolute; top: 104px; left: 0; right: 0;
    display: flex; align-items: center; justify-content: center; gap: 10px;
  }
  .brand__mark { width: 26px; height: 26px; background: var(--brand-blue); }
  .brand__name {
    font-weight: 700; font-size: 38px; line-height: 1; color: var(--ink); letter-spacing: -0.5px;
  }
  .card--back .brand__name { color: var(--on-dark); font-size: 44px; }
  .person {
    position: absolute; top: 156px; left: 0; right: 0; text-align: center;
    text-transform: uppercase;
  }
  .person__name { font-size: 13px; font-weight: 500; color: var(--ink); letter-spacing: 1px; }
  .person__role { font-size: 9px; color: var(--ink-soft); letter-spacing: 1.5px; margin-top: 3px; }
  .contact-list {
    position: absolute; list-style: none; display: flex; flex-direction: column; gap: 8px;
  }
  .contact-list--primary { top: 26px; left: 24px; }
  .contact-list--online { bottom: 26px; right: 40px; }
  .contact-item {
    display: flex; align-items: center; gap: 8px;
    font-size: 8.5px; color: var(--ink-soft);
  }
  .contact-item__icon {
    width: 14px; height: 14px; background: var(--brand-blue); flex: none;
    display: flex; align-items: center; justify-content: center;
  }
  .contact-item__icon svg { width: 10px; height: 10px; fill: var(--card-white); }
</style>
</head>
<body>
<main class="stationery">
  <section class="card card--front">
    <ul class="contact-list contact-list--primary">
      <li class="contact-item">
        <span class="contact-item__icon"><svg viewBox="0 0 10 10"><path d="M5 0.5a3 3 0 0 0-3 3c0 2.3 3 6 3 6s3-3.7 3-6a3 3 0 0 0-3-3zm0 4.2a1.2 1.2 0 1 1 0-2.4 1.2 1.2 0 0 1 0 2.4z"/></svg></span>
        Av. Pierre Dumel 42 CH-1209 Geneva
      </li>
      <li class="contact-item">
        <span class="contact-item__icon"><svg viewBox="0 0 10 10"><path d="M2.2 1l1.6 2-0.9 1a5.5 5.5 0 0 0 2.6 2.6l1-0.9 2 1.6-0.9 1.7C4.3 8.9 1.1 5.7 0.5 1.9z"/></svg></span>
        022 555 0142
      </li>
      <li class="contact-item">
        <span class="contact-item__icon"><svg viewBox="0 0 10 10"><path d="M1 2.5h8v5H1zM1.5 3l3.5 2.5L8.5 3" stroke="#2f8fd8" stroke-width="0.6"/></svg></span>
        mferrand@vexmora.com
      </li>
    </ul>

    <div class="brand">
      <span class="brand__mark"></span>
      <span class="brand__name">vexmora</span>
    </div>

    <div class="person">
      <p class="person__name">Mathieu Ferrand</p>
      <p class="person__role">Associate</p>
    </div>

    <ul class="contact-list contact-list--online">
      <li class="contact-item">
        <span class="contact-item__icon"><svg viewBox="0 0 10 10"><circle cx="5" cy="5" r="3.8" fill="none" stroke="#fff" stroke-width="0.9"/><path d="M1.2 5h7.6M5 1.2c-2 2.2-2 5.4 0 7.6M5 1.2c2 2.2 2 5.4 0 7.6" fill="none" stroke="#fff" stroke-width="0.7"/></svg></span>
        www.vexmora.com
      </li>
      <li class="contact-item">
        <span class="contact-item__icon"><svg viewBox="0 0 10 10"><path d="M3 2l4 3-4 3z"/></svg></span>
        /vexmora
      </li>
      <li class="contact-item">
        <span class="contact-item__icon"><svg viewBox="0 0 10 10"><circle cx="5" cy="5" r="3" fill="none" stroke="#fff" stroke-width="1"/></svg></span>
        @vexmora
      </li>
    </ul>
  </section>

  <section class="card card--back">
    <div class="brand-reverse">
      <span class="brand__name">vexmora</span>
    </div>
  </section>
</main>
</body>
</html>
```